Modern business card and agenda for facilitation and consulting firm -
KESTREL MEDIATION
Professional
Brigitte Halvorsen M.Ed
Managing Director/Facilitator
Suite 400, 20844 157 Avenue Edmonton, Alberta T6K 2W8
brigitte@kestrelmediation.example
www.kestrelmediation.example
PixelHarborStudio PixelHarborStudio
Halvorsen Halvorsen
I will be using the stationary for two purposes: 1. agenda's, proposals, invoices, newsletters 2. workshops so it would be nice to have a black and white version as well as colour Thank you. BRigitte

```html
<!DOCTYPE html>
<html lang="en">
<head>
<meta charset="utf-8">
<title>Kestrel Mediation – Business Card</title>
<link href="https://fonts.googleapis.com/css2?family=Raleway:wght@400;600;800&family=Open+Sans:wght@400;600&display=swap" rel="stylesheet">
<style>
  :root{
    --bg:#e9ecef;
    --card:#ffffff;
    --blue:#3d6893;
    --navy:#2c5580;
    --green:#7cb84a;
    --soft:#c9d6e2;
    --text-light:#f2f6fa;
  }
  html,body{margin:0;padding:0;overflow:hidden;}
  body{width:1200px;height:996px;background:var(--bg);position:relative;font-family:'Open Sans',sans-serif;}
  .card{position:absolute;width:700px;height:400px;background:var(--card);border-radius:22px;overflow:hidden;box-shadow:0 10px 28px rgba(0,0,0,.18);}
  .card--back{left:440px;top:70px;}
  .card--front{left:60px;top:520px;}

  .back-mark{position:absolute;left:40px;top:-70px;width:330px;height:330px;border-radius:50%;background:var(--soft);opacity:.55;}
  .back-web{position:absolute;right:46px;bottom:44px;font-size:17px;letter-spacing:3px;color:var(--navy);}

  .wave{position:absolute;left:0;top:0;width:700px;height:400px;}
  .brand{position:absolute;left:170px;top:46px;display:flex;align-items:center;gap:18px;}
  .brand-dot{width:78px;height:78px;border-radius:50%;background:var(--blue);}
  .brand-name{font-family:'Raleway',sans-serif;font-weight:800;font-size:34px;line-height:1.02;color:var(--navy);letter-spacing:1px;}
  .brand-tagline{font-family:'Raleway',sans-serif;font-weight:800;font-size:11px;color:var(--navy);margin-top:6px;letter-spacing:.5px;}

  .contact{position:absolute;left:300px;top:232px;color:var(--text-light);}
  .contact-name{font-weight:600;font-size:19px;margin:0;}
  .contact-title{font-size:12px;margin:2px 0 12px;}
  .contact-address{position:absolute;left:-210px;top:48px;font-size:11.5px;line-height:1.5;width:190px;}
  .contact-list{list-style:none;margin:0;padding:0;font-size:11.5px;line-height:1.75;}
  .contact-list li{display:flex;align-items:center;gap:8px;}
  .contact-list svg{width:12px;height:12px;fill:var(--text-light);}
</style>
</head>
<body>

<section class="card card--back" aria-label="Card back">
  <div class="back-mark"></div>
  <div class="back-web">www.kestrelmediation.example</div>
</section>

<section class="card card--front" aria-label="Card front">
  <svg class="wave" viewBox="0 0 700 400" aria-hidden="true">
    <path d="M0 200 C200 160 450 245 700 180 L700 400 L0 400 Z" fill="var(--blue)"/>
    <path d="M0 186 C200 146 450 228 700 166" fill="none" stroke="var(--green)" stroke-width="9"/>
  </svg>

  <div class="brand">
    <div class="brand-dot"></div>
    <div>
      <div class="brand-name">KESTREL<br>MEDIATION</div>
      <div class="brand-tagline">Clear Conversations. Lasting Outcomes.</div>
    </div>
  </div>

  <div class="contact">
    <p class="contact-name">Brigitte Halvorsen M.Ed</p>
    <p class="contact-title">Managing Director/Facilitator</p>
    <div class="contact-address">Suite 400, 20844 157 Avenue<br>Edmonton, Alberta T6K 2W8</div>
    <ul class="contact-list">
      <li><svg viewBox="0 0 24 24"><path d="M6.6 10.8a15 15 0 0 0 6.6 6.6l2.2-2.2a1 1 0 0 1 1-.25 11.4 11.4 0 0 0 3.6.57 1 1 0 0 1 1 1V20a1 1 0 0 1-1 1A17 17 0 0 1 3 4a1 1 0 0 1 1-1h3.5a1 1 0 0 1 1 1c0 1.25.2 2.45.57 3.57a1 1 0 0 1-.25 1z"/></svg>780 555 0142</li>
      <li><svg viewBox="0 0 24 24"><path d="M2 5h20v14H2z M2 5l10 8 10-8" fill="none" stroke="#f2f6fa" stroke-width="2"/></svg>brigitte@kestrelmediation.example</li>
      <li><svg viewBox="0 0 24 24"><circle cx="12" cy="12" r="9" fill="none" stroke="#f2f6fa" stroke-width="2"/><path d="M3 12h18M12 3c3 3 3 15 0 18M12 3c-3 3-3 15 0 18" fill="none" stroke="#f2f6fa" stroke-width="1.6"/></svg>www.kestrelmediation.example</li>
    </ul>
  </div>
</section>

</body>
</html>
```